Torvin Electrics Flyer Design Advertising

I am after an A5 Flyer design to help promote my electrical services business.
I would like to have information on what my business offers, photos of electrical work, and specials/deals for an amount of time.

Industry/Entity Type

Electrician

Font styles to use
Sans Serif

Colors
0292cd
33a6d7
85cae6
3176b5
333333
1b1b1b
ffffff
5c5c5c
474747

Requirements
Must have
• Specialising in New homes, renovations and commercial projects
• Contact details:
• ph. 0457 613 948
• email admin@torvinelectrics.com.au
• facebook TorvinElectrics
• Specials/Deals:
• 10% off all electrical services
• or
• Free LED downlights on installation
• *Terms conditions apply
• ALL RESIDENTIAL & COMMERCIAL ELECTRICAL SERVICES
• - New Home installations
• - Commercial projects
• - Shop fit outs
• - Renovations
• - Smoke Detectors
• - Air Conditioning and Ceiling Fans
• - Garden Lighting
• - Oven and Cooktop Installations
• - Power Point installation
• - LED lighting upgrades
• - Security Lighting
• - Switchboard upgrades
• - Test and Tag
• - Commercial Property
• - General Electrical Maintenance

```html
<!DOCTYPE html>
<html lang="en">
<head>
<meta charset="utf-8">
<title>Torvin Electrics Flyer</title>
<link rel="stylesheet" href="https://fonts.googleapis.com/css2?family=Titillium+Web:wght@400;600;700&family=Open+Sans:wght@400;600&display=swap">
<style>
  :root {
    --blue-deep: #0292cd;
    --blue-mid: #33a6d7;
    --blue-light: #85cae6;
    --blue-navy: #3176b5;
    --blue-panel: #1eabe2;
    --blue-ink: #22409a;
    --ink: #333333;
    --ink-dark: #1b1b1b;
    --grey: #5c5c5c;
    --grey-dark: #474747;
    --white: #ffffff;
  }
  * { margin: 0; padding: 0; box-sizing: border-box; }
  html, body { width: 838px; height: 1200px; overflow: hidden; background: var(--white); }
  .flyer { position: relative; width: 838px; height: 1200px; background: var(--white); font-family: "Open Sans", sans-serif; color: var(--ink); }

  .brand { position: absolute; left: 52px; top: 40px; display: flex; align-items: center; gap: 12px; }
  .brand-dot { width: 66px; height: 66px; border-radius: 50%; background: var(--grey-dark); }
  .brand-name { font-family: "Titillium Web", sans-serif; font-weight: 700; font-size: 24px; color: var(--ink); }

  .tagline { position: absolute; right: 35px; top: 46px; text-align: right; font-family: "Titillium Web", sans-serif; font-weight: 700; font-size: 19px; line-height: 24px; color: var(--ink); text-transform: uppercase; }

  .hero-edge { position: absolute; left: 0; top: 143px; width: 33px; height: 512px; background: linear-gradient(180deg, #1a2a3a, #0c4a78 60%, #12243a); }
  .hero-panel { position: absolute; left: 33px; top: 143px; width: 385px; height: 512px; background: var(--blue-panel); color: var(--white); text-align: center; }
  .hero-title { font-family: "Titillium Web", sans-serif; font-weight: 700; font-size: 66px; line-height: 80px; padding-top: 64px; letter-spacing: -0.5px; }
  .hero-title .accent { color: var(--blue-ink); }
  .hero-copy { margin: 40px auto 0; width: 350px; font-size: 11px; line-height: 15px; }
  .hero-web { margin-top: 64px; font-size: 11px; display: flex; justify-content: center; align-items: center; gap: 8px; }

  .hero-photo { position: absolute; left: 418px; top: 143px; width: 420px; height: 512px; background: linear-gradient(160deg, #d9dde0 0%, #b9a48c 40%, #2b3550 75%, #1f2a44 100%); }
  .deal { position: absolute; left: 418px; top: 143px; width: 420px; height: 520px; }

  .photo { position: absolute; left: 32px; width: 386px; height: 180px; }
  .photo-home { top: 677px; background: linear-gradient(180deg, #5c6f84 0%, #b7a993 55%, #3f4a3a 100%); }
  .photo-commercial { top: 880px; background: linear-gradient(180deg, #1e3a6e 0%, #35507e 50%, #2a3b2a 100%); }
  .photo-label { position: absolute; left: 24px; bottom: 12px; font-family: "Titillium Web", sans-serif; font-weight: 700; font-size: 20px; color: var(--white); text-transform: uppercase; text-shadow: 0 1px 3px rgba(0,0,0,.6); }

  .services { position: absolute; left: 463px; top: 672px; }
  .services-title { font-family: "Titillium Web", sans-serif; font-weight: 700; font-size: 21px; line-height: 26px; color: var(--blue-deep); text-transform: uppercase; }
  .service-list { list-style: none; margin-top: 3px; }
  .service-list li { display: flex; align-items: center; gap: 9px; font-family: "Titillium Web", sans-serif; font-weight: 700; font-size: 17px; line-height: 21.7px; color: var(--ink); text-transform: uppercase; }
  .tick { width: 7px; height: 7px; flex: none; }

  .phone { position: absolute; left: 461px; top: 986px; display: flex; align-items: center; gap: 10px; font-family: "Titillium Web", sans-serif; font-size: 42px; line-height: 48px; color: var(--blue-deep); letter-spacing: 1px; }
  .site { position: absolute; left: 461px; top: 1041px; display: flex; align-items: center; gap: 10px; font-family: "Titillium Web", sans-serif; font-weight: 700; font-size: 17px; color: var(--ink); text-transform: uppercase; }

  .footer { position: absolute; left: 0; top: 1083px; width: 838px; height: 117px; background: var(--ink-dark); color: var(--white); font-size: 15px; line-height: 20px; }
  .footer-item { position: absolute; top: 32px; display: flex; gap: 16px; align-items: flex-start; }
  .footer-address { left: 30px; }
  .footer-contact { left: 461px; }
</style>
</head>
<body>
<main class="flyer">
  <header>
    <div class="brand"><span class="brand-dot"></span><span class="brand-name">Torvin Electrics</span></div>
    <p class="tagline">Specialising in new homes,<br>renovations and commercial projects</p>
  </header>

  <section>
    <div class="hero-edge" role="img" aria-label="Dark blue electrical equipment background"></div>
    <div class="hero-panel">
      <h1 class="hero-title">EXPERT<br><span class="accent">ELECTRICAL</span><br>SERVICES</h1>
      <p class="hero-copy">Lorem Ipsum is simply dummy text of the printing and typesetting industry. Lorem Ipsum has been the industry's standard dummy text ever since the 1500s,</p>
      <p class="hero-web">
        <svg width="9" height="9" viewBox="0 0 10 10"><circle cx="5" cy="5" r="4.5" fill="none" stroke="#fff"/><path d="M0.5 5h9M5 .5v9" stroke="#fff"/></svg>
        www.torvinelectrics.com.au
      </p>
    </div>
    <div class="hero-photo" role="img" aria-label="Photo of a smiling electrician in a hard hat and goggles holding an orange cable"></div>
    <svg class="deal" viewBox="0 0 420 520">
      <polygon points="112,450 138,430 222,425" fill="var(--blue-navy)"/>
      <polygon points="150,438 300,425 300,480 160,494" fill="var(--blue-navy)" transform="translate(0,-60)"/>
      <polygon points="37,357 357,310 367,420 42,452" fill="var(--blue-light)" opacity=".95"/>
      <polygon points="37,357 357,310 367,420 42,452" fill="var(--blue-mid)" opacity=".55"/>
      <polygon points="42,452 270,430 150,520 112,520" fill="var(--blue-light)"/>
      <polyline points="45,370 350,325" stroke="var(--blue-navy)" stroke-dasharray="3 3" fill="none"/>
      <polygon points="270,335 375,320 375,405 270,420" fill="var(--blue-navy)"/>
      <g transform="rotate(-8 200 380)" font-family="Titillium Web, sans-serif" font-weight="700">
        <text x="58" y="369" font-size="17" fill="var(--blue-navy)">SPECIALS DEALS</text>
        <text x="52" y="402" font-size="29" fill="var(--white)">ALL ELECTRICAL</text>
        <text x="52" y="440" font-size="29" fill="var(--white)">SERVICES</text>
        <text x="276" y="368" font-size="30" fill="var(--white)">UPTO</text>
        <text x="274" y="408" font-size="40" fill="var(--white)">10</text>
        <text x="320" y="390" font-size="18" fill="var(--white)">%</text>
        <text x="322" y="404" font-size="11" fill="var(--white)">OFF</text>
      </g>
    </svg>
  </section>

  <section>
    <div class="photo photo-home" role="img" aria-label="Photo of a lit two-storey new home at dusk">
      <span class="photo-label">New Home Installations</span>
    </div>
    <div class="photo photo-commercial" role="img" aria-label="Photo of a modern building lit at night with palm trees">
      <span class="photo-label">Commercial Projects</span>
    </div>
  </section>

  <section class="services">
    <h2 class="services-title">All residential &amp; commercial<br>electrical services</h2>
    <ul class="service-list">
      <li><svg class="tick" viewBox="0 0 8 8"><circle cx="4" cy="4" r="4" fill="#6cb33f"/><path d="M2 4l1.5 1.5L6 3" stroke="#fff" fill="none"/></svg>Renovations</li>
      <li><svg class="tick" viewBox="0 0 8 8"><circle cx="4" cy="4" r="4" fill="#6cb33f"/><path d="M2 4l1.5 1.5L6 3" stroke="#fff" fill="none"/></svg>Smoke Detectors</li>
      <li><svg class="tick" viewBox="0 0 8 8"><circle cx="4" cy="4" r="4" fill="#6cb33f"/><path d="M2 4l1.5 1.5L6 3" stroke="#fff" fill="none"/></svg>Air Conditioning and Ceiling Fans</li>
      <li><svg class="tick" viewBox="0 0 8 8"><circle cx="4" cy="4" r="4" fill="#6cb33f"/><path d="M2 4l1.5 1.5L6 3" stroke="#fff" fill="none"/></svg>Garden Lighting</li>
      <li><svg class="tick" viewBox="0 0 8 8"><circle cx="4" cy="4" r="4" fill="#6cb33f"/><path d="M2 4l1.5 1.5L6 3" stroke="#fff" fill="none"/></svg>Oven and Cooktop Installations</li>
      <li><svg class="tick" viewBox="0 0 8 8"><circle cx="4" cy="4" r="4" fill="#6cb33f"/><path d="M2 4l1.5 1.5L6 3" stroke="#fff" fill="none"/></svg>Power Point Installation</li>
      <li><svg class="tick" viewBox="0 0 8 8"><circle cx="4" cy="4" r="4" fill="#6cb33f"/><path d="M2 4l1.5 1.5L6 3" stroke="#fff" fill="none"/></svg>LED Lighting Upgrades</li>
      <li><svg class="tick" viewBox="0 0 8 8"><circle cx="4" cy="4" r="4" fill="#6cb33f"/><path d="M2 4l1.5 1.5L6 3" stroke="#fff" fill="none"/></svg>Security Lighting</li>
      <li><svg class="tick" viewBox="0 0 8 8"><circle cx="4" cy="4" r="4" fill="#6cb33f"/><path d="M2 4l1.5 1.5L6 3" stroke="#fff" fill="none"/></svg>Switchboard Upgrades</li>
      <li><svg class="tick" viewBox="0 0 8 8"><circle cx="4" cy="4" r="4" fill="#6cb33f"/><path d="M2 4l1.5 1.5L6 3" stroke="#fff" fill="none"/></svg>Test and Tag</li>
      <li><svg class="tick" viewBox="0 0 8 8"><circle cx="4" cy="4" r="4" fill="#6cb33f"/><path d="M2 4l1.5 1.5L6 3" stroke="#fff" fill="none"/></svg>Commercial Property</li>
      <li><svg class="tick" viewBox="0 0 8 8"><circle cx="4" cy="4" r="4" fill="#6cb33f"/><path d="M2 4l1.5 1.5L6 3" stroke="#fff" fill="none"/></svg>General Electrical Maintenance</li>
    </ul>
  </section>

  <p class="phone">
    <svg width="36" height="36" viewBox="0 0 36 36"><rect width="36" height="36" rx="7" fill="var(--blue-deep)"/><path d="M11 8c2 0 3 4 3 5s-2 2-2 3c1 3 4 6 7 7 1 0 2-2 3-2s5 1 5 3-3 4-5 4C14 28 8 20 8 12c0-2 1-4 3-4z" fill="var(--white)"/></svg>
    0457 613 948
  </p>
  <p class="site">
    <svg width="12" height="12" viewBox="0 0 12 12"><circle cx="6" cy="6" r="5.3" fill="none" stroke="var(--ink)" stroke-width="1.2"/><path d="M.7 6h10.6M6 .7v10.6M2 3h8M2 9h8" stroke="var(--ink)" fill="none"/></svg>
    www.torvinelectrics.com.au
  </p>

  <footer class="footer">
    <div class="footer-item footer-address">
      <svg width="16" height="24" viewBox="0 0 16 24"><path d="M8 0a8 8 0 0 1 8 8c0 6-8 16-8 16S0 14 0 8a8 8 0 0 1 8-8z" fill="var(--white)"/><circle cx="8" cy="8" r="3" fill="var(--ink-dark)"/></svg>
      <p>TorvinElectrics<br>1234 Newhall Ln, Example, TX 5678</p>
    </div>
    <div class="footer-item footer-contact">
      <svg width="20" height="14" viewBox="0 0 20 14" style="margin-top:4px"><rect x=".7" y=".7" width="18.6" height="12.6" fill="none" stroke="var(--white)" stroke-width="1.4"/><path d="M1 1l9 7 9-7M1 13l7-6M19 13l-7-6" stroke="var(--white)" stroke-width="1.4" fill="none"/></svg>
      <p>admin@torvinelectrics.com.au<br>facebook:&nbsp; TorvinElectrics</p>
    </div>
  </footer>
</main>
</body>
</html>
```